Flyer-Design für Software für Gebäudedienstleister
Zielgruppe
Software für Gebäudedienstleister,
Softwarevertrieb, Durchführung von Schulungen,
Aufgabenstellung
Erstellt werden soll eine Din A4 Seite mit Wickelfalz (6Seiten)
Für den Neustart einer Software für Gebäudedienstleister möchten wir einen modernen
Flyer mit ansprechendem Text anfertigen lassen.
Die Software funktioniert Online oder Lokal.
Ein Tablet-Service wird angeboten.
Eine elektronische Planungstafel bietet die Software.
Terminplanung mittels "Drag & Drop" möglich
1-Klick Funktion in der Rückmeldung von Arbeitsscheinen und in der anschließenden Fakturierung.
Durchführung von Schulungen Akademie
Texte:
1.Fakturierung
Mit Vantoruk® Faktura liefern wir Ihnen ein leicht zu bedienendes Modul
Die Vantoruk®Fakturierungssoftware zeichnet sich durch einfache Handhabung aus:
Moderne Faktura Software
Leicht zu bedienen
Gut strukturierte Benutzeroberfläche
Praxisorientierte Funktionen
Sofort einsatzbereit
1-Klick Fakturierung
Mit Vantoruk® fakturieren Sie schnell und effektiv.
2. Personaleinsatzplanung Drag & Drop
Die Einsatzplanung erfolgt in Vantoruk® mit nur wenigen Schritten.
Dabei berücksichtigt das System z.B. die Regionen, in denen Sie
tätig sind und verhindert somit unnötige Fahrzeiten.
Pausen werden automatisch erfasst. Touren planen Sie bereits
bequem per Drag & Drop auf dem Gesamtkalender.
3. Planungstafel
Mit Vantoruk® planen Sie einfach und schnell Termine.
Mit unserer elektronischen Planungstafel behalten Sie immer
einen optimalen Überblick über Ihre Ressourcen.
Vantoruk® ist die intelligente Lösung für Ihre Personaleinsatzplanung.
4. Tabletservice
Bieten Sie Ihrem Kunden mit Vantoruk® einen echten Mehrwert
Sie möchten Ihrem Kunden gegenüber als modernes und zielorientiertes
Unternehmen auftreten?
Setzen Sie ab jetzt unseren Tablet-Service in Ihrem Betrieb ein.
Egal ob Arbeitsschein zurückmelden, schnell ein Foto vom Wintergarten,
oder eine Unterschrift fü..

```html
<!DOCTYPE html>
<html lang="de">
<head>
<meta charset="utf-8">
<title>Vantoruk – Flyer Gebäudedienstleister</title>
<link href="https://fonts.googleapis.com/css2?family=Questrial&display=swap" rel="stylesheet">
<style>
:root{
  --olive:#a2b11f;
  --slate:#505a6b;
  --ink:#4b505c;
  --text:#555a63;
  --paper:#ffffff;
  --bg:#ffffff;
}
*{box-sizing:border-box;margin:0;padding:0}
html,body{width:1200px;height:1200px;overflow:hidden;background:var(--bg)}
body{position:relative;font-family:"Questrial",sans-serif;color:var(--text)}
.spread{position:absolute;left:269px;width:1085px;height:767px;background:var(--paper);
  transform:scale(.625);transform-origin:0 0;box-shadow:4px 6px 10px rgba(0,0,0,.35);overflow:hidden}
.spread--outside{top:61px}
.spread--inside{top:622px}
.shapes{position:absolute;left:0;top:0;width:1085px;height:767px}
.abs{position:absolute}
.hl{color:var(--olive);font-weight:700}
.title{position:absolute;font-size:38px;font-weight:400;color:var(--ink);white-space:nowrap}
.title--olive{color:var(--olive)}
.copy{position:absolute;font-size:11.5px;line-height:1.2;color:var(--text)}
.copy p{margin-bottom:10px}
.bullets{list-style:none}
.bullets li{position:relative;padding-left:20px;margin-bottom:6.5px}
.bullets li::before{content:"";position:absolute;left:2px;top:3px;width:7px;height:7px;background:var(--slate);transform:rotate(45deg)}
.photo{position:absolute}
.cover-title{position:absolute;left:735px;top:196px;color:#fff;line-height:1}
.cover-title .big{font-size:58px;display:block;margin-bottom:8px}
.cover-title .mid{font-size:44px;display:block;margin-bottom:8px}
.cover-title .sm{font-size:34px;display:block;margin-bottom:5px}
.address{position:absolute;left:403px;top:610px;color:#fff;font-size:12.5px;line-height:1.18}
.brand{position:absolute;left:815px;top:640px;color:#fff;font-size:40px;display:flex;align-items:center;gap:10px}
.brand .dot{width:14px;height:14px;border-radius:50%;background:var(--olive)}
.features{position:absolute;left:420px;top:346px;list-style:none;font-size:16.5px;color:var(--ink)}
.features li{position:relative;padding-left:28px;height:37px}
.features li::before{content:"";position:absolute;left:2px;top:4px;width:10px;height:10px;background:var(--olive);transform:rotate(45deg)}
.academy{position:absolute;left:755px;top:98px;width:320px;font-size:11.5px;line-height:1.18;hyphens:auto}
.academy .pic{float:left;width:143px;height:130px;margin:0 7px 4px 0;background:linear-gradient(160deg,#8da0b8 0%,#6b5a50 55%,#8b8780 100%)}
.academy h3{font-weight:400;font-size:11.5px;color:var(--olive);margin-bottom:18px}
.academy p{margin:0}
.seminar{position:absolute;left:795px;top:292px;font-size:11.5px}
.seminar .lead{margin:0 0 13px 12px}
.seminar .bullets li{margin-bottom:6.8px}
.tablet-copy{position:absolute;left:738px;top:585px;width:188px;font-size:11px;line-height:1.15;letter-spacing:-.15px;hyphens:auto}
.tablet-copy p{margin-bottom:9px}
.tablet-more{position:absolute;left:738px;top:701px;width:340px;font-size:11px;line-height:1.15;letter-spacing:-.15px;hyphens:auto}
</style>
</head>
<body>

<section class="spread spread--outside">
  <svg class="shapes" viewBox="0 0 1085 767" aria-hidden="true">
    <polygon points="282,0 362,0 362,108" fill="var(--slate)"/>
    <polyline points="15,0 15,73 330,73" fill="none" stroke="var(--olive)" stroke-width="1.5"/>
    <polygon points="362,392 402,357 708,662 605,767 362,767" fill="var(--slate)"/>
    <polygon points="1085,392 1048,357 740,662 843,767 1085,767" fill="var(--slate)"/>
    <polygon points="723,35 1030,340 730,647 418,340" fill="var(--olive)"/>
    <polygon points="700,35 1028,315 745,647 418,362" fill="none" stroke="var(--slate)" stroke-width="1.3"/>
  </svg>
  <div class="photo" role="img" aria-label="Foto: moderne geschwungene Bürofassade mit Hochhäusern"
       style="left:740px;top:0;width:345px;height:322px;clip-path:polygon(0 0,100% 0,100% 100%);background:linear-gradient(200deg,#6f9fd0 0%,#b9c7d4 45%,#d9dde1 100%)"></div>

  <h1 class="title" style="left:45px;top:22px">Fakturierung</h1>
  <div class="copy" style="left:45px;top:120px;width:270px">
    <p>Mit <span class="hl">Vantoruk® Faktura</span> liefern wir Ihnen ein leicht zu bedienendes Modul.</p>
    <p>Die <span class="hl">Vantoruk®Fakturierungssoftware</span> zeichnet sich durch einfache Handhabung aus:</p>
  </div>
  <ul class="copy bullets" style="left:25px;top:199px">
    <li>Moderne Faktura Software</li>
    <li>Leicht zu bedienen</li>
    <li>Gut strukturierte Benutzeroberfläche</li>
    <li>Praxisorientierte Funktionen</li>
    <li>Sofort einsatzbereit</li>
    <li>1-Klick Fakturierung</li>
  </ul>
  <p class="copy" style="left:45px;top:340px">Mit <span class="hl">Vantoruk®</span> fakturieren Sie schnell und effektiv.</p>
  <div class="photo" role="img" aria-label="Foto: Schreibtisch mit Monitor voller Balkendiagramme, Laptop und Kaffeetasse"
       style="left:0;top:442px;width:362px;height:270px;background:linear-gradient(180deg,#eef0f2 0%,#e2e5e8 60%,#f4f5f6 100%)"></div>

  <div class="cover-title">
    <span class="big">DIE</span>
    <span class="mid">Software</span>
    <span class="sm">für</span>
    <span class="sm">Gebäude-</span>
    <span class="sm">dienstleister</span>
  </div>
  <div class="address">Adresse<br>Strasse<br>PLZ, Ort<br>Tel<br>Mail<br>www</div>
  <div class="brand"><span class="dot"></span>Vantoruk®</div>
</section>

<section class="spread spread--inside">
  <svg class="shapes" viewBox="0 0 1085 767" aria-hidden="true">
    <polygon points="0,0 22,0 57,35 0,88" fill="var(--olive)"/>
    <polyline points="57,0 348,0 348,73 57,73" fill="none" stroke="var(--slate)" stroke-width="1.2"/>
    <polygon points="362,350 362,515 278,430" fill="var(--slate)"/>
    <polyline points="278,430 15,430 15,503 362,503" fill="none" stroke="var(--olive)" stroke-width="1.5"/>
    <polyline points="362,345 475,210 725,420" fill="none" stroke="var(--slate)" stroke-width="1.3"/>
    <polyline points="362,365 500,210 725,400" fill="none" stroke="var(--olive)" stroke-width="1.3"/>
    <line x1="362" y1="685" x2="465" y2="767" stroke="var(--slate)" stroke-width="1.3"/>
    <line x1="362" y1="695" x2="450" y2="767" stroke="var(--olive)" stroke-width="1.3"/>
    <line x1="725" y1="585" x2="555" y2="767" stroke="var(--olive)" stroke-width="1.3"/>
    <line x1="725" y1="600" x2="575" y2="767" stroke="var(--slate)" stroke-width="1.3"/>
    <polyline points="738,0 738,67 1025,67" fill="none" stroke="var(--olive)" stroke-width="1.5"/>
    <polygon points="988,0 1085,0 1085,122" fill="var(--slate)"/>
    <polygon points="725,435 810,510 725,600" fill="var(--olive)"/>
    <polyline points="755,492 1070,492 1070,568 755,568" fill="none" stroke="var(--slate)" stroke-width="1.2"/>
  </svg>

  <h2 class="title title--olive" style="left:78px;top:16px">Planungstafel</h2>
  <div class="copy" style="left:26px;top:96px;width:320px">
    <p>Mit <span class="hl">Vantoruk®</span> planen Sie einfach und schnell Termine.</p>
    <p>Mit unserer elektronischen Planungstafel behalten Sie immer einen optimalen Überblick über Ihre Ressourcen.</p>
    <p><span class="hl">Vantoruk®</span> ist die intelligente Lösung für Ihre Personal&shy;einsatzplanung.</p>
  </div>

  <svg class="abs" style="left:15px;top:210px" width="333" height="112" viewBox="0 0 333 112" aria-label="Terminplaner-Tabelle">
    <text x="2" y="6" font-size="6" font-weight="700" fill="#333" font-family="Questrial,sans-serif">Terminplaner</text>
    <g fill="var(--olive)">
      <rect x="15" y="12" width="40" height="8"/><rect x="58" y="12" width="33" height="8"/><rect x="94" y="12" width="18" height="8"/>
      <rect x="115" y="12" width="13" height="8"/><rect x="131" y="12" width="13" height="8"/><rect x="147" y="12" width="13" height="8"/><rect x="163" y="12" width="13" height="8"/>
      <rect x="240" y="12" width="15" height="8"/><rect x="258" y="12" width="15" height="8"/><rect x="276" y="12" width="15" height="8"/><rect x="294" y="12" width="15" height="8"/>
    </g>
    <g font-size="4" fill="#fff" font-family="Questrial,sans-serif">
      <text x="17" y="18">Wochenansicht</text><text x="60" y="18">Tagesansicht</text><text x="96" y="18">Heute</text>
    </g>
    <text x="190" y="18" font-size="4.5" fill="#555" font-family="Questrial,sans-serif">Freitag, 14.04.2017</text>
    <rect x="2" y="24" width="330" height="86" fill="none" stroke="#aaa" stroke-width=".6"/>
    <text x="210" y="30" font-size="4.5" font-weight="700" fill="#333" font-family="Questrial,sans-serif">Freitag, 14.04.2017</text>
    <g stroke="#ccc" stroke-width=".4">
      <line x1="68" y1="24" x2="68" y2="110"/><line x1="68" y1="33" x2="332" y2="33"/>
      <line x1="2" y1="40" x2="332" y2="40"/><line x1="2" y1="50" x2="332" y2="50"/><line x1="2" y1="60" x2="332" y2="60"/>
      <line x1="2" y1="70" x2="332" y2="70"/><line x1="2" y1="80" x2="332" y2="80"/><line x1="2" y1="90" x2="332" y2="90"/><line x1="2" y1="100" x2="332" y2="100"/>
      <line x1="96" y1="33" x2="96" y2="110"/><line x1="124" y1="33" x2="124" y2="110"/><line x1="152" y1="33" x2="152" y2="110"/><line x1="180" y1="33" x2="180" y2="110"/>
      <line x1="208" y1="33" x2="208" y2="110"/><line x1="236" y1="33" x2="236" y2="110"/><line x1="264" y1="33" x2="264" y2="110"/><line x1="292" y1="33" x2="292" y2="110"/><line x1="320" y1="33" x2="320" y2="110"/>
    </g>
    <rect x="124" y="40" width="7" height="70" fill="#f2c8cc"/><rect x="208" y="40" width="7" height="70" fill="#f2c8cc"/><rect x="290" y="40" width="7" height="70" fill="#f2c8cc"/>
    <rect x="306" y="42" width="26" height="7" fill="#7fc3dc"/>
    <rect x="96" y="52" width="28" height="7" fill="#c9b98a"/><rect x="270" y="52" width="24" height="7" fill="#c9b98a"/>
    <rect x="131" y="62" width="26" height="7" fill="#bfe3ee"/><rect x="218" y="62" width="26" height="7" fill="#bfe3ee"/>
    <rect x="96" y="72" width="160" height="7" fill="#5aaed6"/>
    <rect x="290" y="82" width="26" height="7" fill="#bfe3ee"/>
    <g font-size="4" fill="#444" font-family="Questrial,sans-serif">
      <text x="5" y="46">Lenz, Adrian</text><text x="5" y="56">Roth, Selma</text><text x="5" y="66">Kaya, Tomas</text>
      <text x="5" y="76">Vogt, Milan</text><text x="5" y="86">Beck, Hanna</text><text x="5" y="96">Diverse</text>
    </g>
  </svg>

  <h2 class="title" style="left:23px;top:443px">Drag &amp; Drop</h2>
  <div class="copy" style="left:29px;top:530px;width:310px">
    <p>Die Einsatzplanung erfolgt in <span class="hl">Vantoruk®</span> mit nur wenigen Schritten. Dabei berücksichtigt das System z.B. die Regionen, in denen Sie tätig sind und verhindert somit unnötige Fahrzeiten. Pausen werden automatisch erfasst.</p>
    <p>Touren planen Sie bereits bequem per Drag &amp; Drop auf dem Gesamtkalender.</p>
  </div>

  <svg class="abs" style="left:15px;top:643px" width="333" height="112" viewBox="0 0 333 112" aria-label="Terminplaner-Tabelle mit zwei Tagen">
    <text x="2" y="6" font-size="6" font-weight="700" fill="#333" font-family="Questrial,sans-serif">Terminplaner</text>
    <g fill="var(--olive)">
      <rect x="32" y="12" width="40" height="8"/><rect x="75" y="12" width="33" height="8"/><rect x="111" y="12" width="18" height="8"/>
      <rect x="132" y="12" width="13" height="8"/><rect x="148" y="12" width="13" height="8"/><rect x="164" y="12" width="13" height="8"/>
      <rect x="240" y="12" width="15" height="8"/><rect x="258" y="12" width="15" height="8"/><rect x="276" y="12" width="15" height="8"/>
    </g>
    <text x="190" y="18" font-size="4.5" fill="#555" font-family="Questrial,sans-serif">Freitag, 14.04.2017</text>
    <rect x="2" y="24" width="330" height="86" fill="none" stroke="#aaa" stroke-width=".6"/>
    <g font-size="4.5" font-weight="700" fill="#333" font-family="Questrial,sans-serif">
      <text x="72" y="30">Donnerstag, 13.04.2017</text><text x="245" y="30">Freitag, 14.04.2017</text>
    </g>
    <g stroke="#ccc" stroke-width=".4">
      <line x1="68" y1="24" x2="68" y2="110"/><line x1="200" y1="24" x2="200" y2="110"/><line x1="68" y1="33" x2="332" y2="33"/>
      <line x1="2" y1="40" x2="332" y2="40"/><line x1="2" y1="50" x2="332" y2="50"/><line x1="2" y1="60" x2="332" y2="60"/>
      <line x1="2" y1="70" x2="332" y2="70"/><line x1="2" y1="80" x2="332" y2="80"/><line x1="2" y1="90" x2="332" y2="90"/><line x1="2" y1="100" x2="332" y2="100"/>
    </g>
    <rect x="90" y="40" width="6" height="70" fill="#f2c8cc"/><rect x="170" y="40" width="6" height="70" fill="#f2c8cc"/><rect x="255" y="40" width="6" height="70" fill="#f2c8cc"/>
    <rect x="306" y="42" width="26" height="7" fill="#7fc3dc"/>
    <rect x="203" y="52" width="14" height="7" fill="#c9b98a"/><rect x="280" y="52" width="24" height="7" fill="#c9b98a"/>
    <rect x="218" y="62" width="14" height="7" fill="#bfe3ee"/><rect x="263" y="62" width="14" height="7" fill="#bfe3ee"/>
    <rect x="203" y="72" width="80" height="7" fill="#5aaed6"/>
    <rect x="293" y="82" width="14" height="7" fill="#bfe3ee"/>
    <g font-size="4" fill="#444" font-family="Questrial,sans-serif">
      <text x="5" y="46">Lenz, Adrian</text><text x="5" y="56">Roth, Selma</text><text x="5" y="66">Kaya, Tomas</text>
      <text x="5" y="76">Vogt, Milan</text><text x="5" y="86">Beck, Hanna</text><text x="5" y="96">Diverse</text>
    </g>
  </svg>

  <div class="photo" role="img" aria-label="Foto: Mann hinter einer Glaswand mit grünen Haftnotizen"
       style="left:377px;top:0;width:347px;height:192px;background:linear-gradient(90deg,#9cc43a 0%,#dfe3df 50%,#9cc43a 100%)"></div>

  <ul class="features">
    <li>Online oder Lokal</li>
    <li>Personaleinsatzplanung</li>
    <li>Kunden, Objekte, Auftrag</li>
    <li>Fakturierung</li>
    <li>Artikelverkauf</li>
    <li>Wartungsplaner</li>
    <li>Datenschnittstellen</li>
    <li>Akademie, Schulungen</li>
  </ul>

  <h2 class="title" style="left:755px;top:13px">Akademie</h2>
  <div class="academy">
    <div class="pic" role="img" aria-label="Foto: modernes Bürogebäude mit Glasfassade"></div>
    <h3><b>Vantoruk®</b> ENTRYSCHULUNG<br>FÜR EINSTEIGER 1 TAG</h3>
    <p>In unserem 1 tägigen Seminar erlernen Sie zunächst die grundlegenden Strukturen der Software. Ziel ist es Stammdaten zu pflegen und eine Übersicht über alle Funktionen zu erhalten. Auch erlernen Sie die einzelnen Module und deren Zusammenspiel in <span class="hl">Vantoruk®</span>. Nach Abschluss der Schulung sind Sie in der Lage strukturiert Kunden, Objekte und Aufträge anzulegen.</p>
  </div>
  <div class="seminar">
    <p class="lead">Seminarinhalt:</p>
    <ul class="bullets">
      <li>Anlegen von Stammdaten</li>
      <li>Interessenten, Kunden, Objekte</li>
      <li>Angebote erstellen</li>
      <li>Aufträge erstellen</li>
      <li>Personaleinsatzplanung</li>
      <li>Arbeitsscheine</li>
      <li>Rückmeldung</li>
      <li>Faktura</li>
    </ul>
  </div>

  <h2 class="title title--olive" style="left:830px;top:503px">Tabletservice</h2>
  <div class="tablet-copy">
    <p>Bieten Sie Ihrem Kunden mit <span class="hl">Vantoruk®</span> einen echten Mehrwert.</p>
    <p>Sie möchten Ihrem Kunden gegen&shy;über als modernes und zielorien&shy;tiertes Unternehmen auftreten? Setzen Sie ab jetzt unseren Tablet-Service in Ihrem Betrieb ein.</p>
  </div>
  <div class="photo" role="img" aria-label="Illustration: Tablet mit Formular auf grünem Grund"
       style="left:930px;top:586px;width:140px;height:89px;background:linear-gradient(135deg,#6fa02e 0%,#8dbb3a 100%)"></div>
  <p class="tablet-more">Egal ob Arbeitsschein zurückmelden, schnell ein Foto vom Wintergarten, oder eine Unterschrift für eine Haftungsbeschrän&shy;kung vor Ort? Mit dem Tablet-Service in <span class="hl">Vantoruk®</span> erscheinen Sie mit Ihrem Unternehmen immer zukunftsorientiert.</p>
</section>

</body>
</html>
```